依頼詳細
■対象となるページ
https://kirameki-jutaku.jp/articles/-/584213

■概要
ルビーハウス住宅研究会「住宅ローン金利ランキング」のデザイン改修のご依頼になります。ユーザーにとって情報が分かりやすく受け取れ、次のアクション(ボタンクリック)につながるようなデザインを希望します。

■ご提出いただくデザイン
PC、スマホ両方のデザイン案

■ページ数
2ページ+4つのタブ(PC、スマホそれぞれ)

■依頼詳細、変更可能範囲

```html
<!DOCTYPE html>
<html lang="ja">
<head>
<meta charset="utf-8">
<title>住宅ローン 詳細タブ</title>
<link rel="stylesheet" href="https://fonts.googleapis.com/css2?family=Noto+Sans+JP:wght@400;500;700;900&display=swap">
<style>
:root{
  --orange:#f29300;
  --orange-light:#f8b440;
  --orange-dark:#e07a00;
  --line:#eba246;
  --label-bg:#fde8c2;
  --tab-bg:#fdf3e1;
  --text:#333333;
  --sub:#555555;
  --white:#ffffff;
}
*{box-sizing:border-box;margin:0;padding:0}
html,body{width:1200px;height:4884px;overflow:hidden;background:var(--white)}
body{font-family:"Noto Sans JP",sans-serif;color:var(--text);position:relative}
.panel{position:absolute;left:0;width:1200px}
.tabs{display:flex;height:88px;margin:0 20px;background:var(--tab-bg);border-bottom:6px solid var(--orange)}
.tab{flex:1;display:flex;align-items:center;justify-content:center;font-size:24px;font-weight:700;color:var(--text);border-right:2px solid #f0d6a8}
.tab:last-child{border-right:none}
.tab.is-active{background:var(--orange);color:var(--text)}
.frame{position:absolute;left:20px;right:20px;top:88px;bottom:0;border:8px solid var(--orange);border-top:none;border-radius:0 0 40px 40px;background:var(--white)}
.frame-title{margin:0 40px;padding:36px 0 22px;text-align:center;font-size:44px;font-weight:900;color:var(--orange);border-bottom:4px solid var(--orange)}
.spec{position:absolute;left:80px;right:80px;border-collapse:collapse;width:1000px}
.spec th,.spec td{border:3px solid var(--line);font-size:23px;line-height:1.45;vertical-align:middle}
.spec th{background:var(--label-bg);text-align:left;font-weight:700;padding:0 24px}
.spec td{padding:14px 28px;font-weight:500}
.note{display:block;font-size:17px;color:var(--sub);line-height:1.45;font-weight:400}
.rate{display:block;font-size:25px;font-weight:500;margin:10px 0 8px}
.center{text-align:center}
.list{list-style:none}
.list li{padding-left:24px;text-indent:-24px}
.more{position:absolute;left:300px;width:600px;height:140px;border-radius:70px;background:linear-gradient(#f9b346,var(--orange) 55%,var(--orange-dark));box-shadow:0 6px 0 #c9640a;display:flex;align-items:center;justify-content:center;gap:56px;color:var(--white);font-size:40px;font-weight:700;text-decoration:none}
.more svg{width:28px;height:32px}
</style>
</head>
<body>

<section class="panel" style="top:0;height:1180px">
  <nav class="tabs"><div class="tab">特徴・評判</div><div class="tab is-active">諸費用</div><div class="tab">審査基準</div><div class="tab">団体信用生命保険</div></nav>
  <div class="frame">
    <h2 class="frame-title">諸費用</h2>
  </div>
  <table class="spec" style="top:228px">
    <colgroup><col style="width:340px"><col></colgroup>
    <tr style="height:64px"><th>手数料（税込）</th><td class="center">融資額×2.20%(税込)</td></tr>
    <tr style="height:156px"><th>保証料</th><td>0円(審査の結果、保証会社を利用する場合があるが、保証料相当額は金利に含まれており、別途、保証料は発生しない)</td></tr>
    <tr style="height:80px"><th>繰上返済手数料（一部）</th><td class="center">0円(1円以上1円単位)</td></tr>
    <tr style="height:124px"><th>繰上返済手数料(全額)</th><td>・変動金利／0円<br>・固定金利／3万3000円(税込)</td></tr>
  </table>
  <a class="more" href="https://kirameki-jutaku.jp/articles/-/584213" style="top:990px">詳細を見る<svg viewBox="0 0 28 32"><path d="M2 2 L26 16 L2 30Z" fill="#fff"/></svg></a>
</section>

<section class="panel" style="top:1220px;height:1640px">
  <nav class="tabs"><div class="tab">特徴・評判</div><div class="tab">諸費用</div><div class="tab is-active">審査基準</div><div class="tab">団体信用生命保険</div></nav>
  <div class="frame">
    <h2 class="frame-title">審査基準</h2>
  </div>
  <table class="spec" style="top:260px">
    <colgroup><col style="width:400px"><col></colgroup>
    <tr style="height:66px"><th>借入額</th><td>500万円以上、2億円以下</td></tr>
    <tr style="height:66px"><th>借入期間</th><td>1年以上35年以内(1ヶ月単位)</td></tr>
    <tr style="height:66px"><th>融資を受けられるエリア</th><td>全国</td></tr>
    <tr style="height:284px"><th>使いみち</th><td>本人または家族が住むための以下の資金<ul class="list"><li>・戸建・マンション(中古物件含む)の購入資金</li><li>・戸建の新築資金</li><li>・他の金融機関で現在借入中の住宅ローンのお借換え(住宅ローンとリフォームローンの一括での借り換えを含む)資金</li><li>・上記に伴う諸費用</li></ul></td></tr>
    <tr style="height:66px"><th>年収(給与所得者)</th><td>200万円以上</td></tr>
    <tr style="height:66px"><th>勤続年数(給与所得者)</th><td>—</td></tr>
    <tr style="height:66px"><th>年収(個人事業主等)</th><td>200万円以上</td></tr>
    <tr style="height:66px"><th>事業年数(個人事業主等)</th><td>—</td></tr>
    <tr style="height:66px"><th>年齢(借入時)</th><td>満18歳以上〜満65歳未満</td></tr>
    <tr style="height:66px"><th>年齢(完済時)</th><td>満80歳の誕生日まで</td></tr>
    <tr style="height:66px"><th>その他条件</th><td>—</td></tr>
  </table>
  <a class="more" href="https://kirameki-jutaku.jp/articles/-/584213" style="top:1440px">詳細を見る<svg viewBox="0 0 28 32"><path d="M2 2 L26 16 L2 30Z" fill="#fff"/></svg></a>
</section>

<section class="panel" style="top:2940px;height:1944px">
  <nav class="tabs"><div class="tab">特徴・評判</div><div class="tab">諸費用</div><div class="tab">審査基準</div><div class="tab is-active">団体信用生命保険</div></nav>
  <div class="frame">
    <h2 class="frame-title">団体信用生命保険</h2>
  </div>
  <table class="spec" style="top:240px">
    <colgroup><col style="width:400px"><col></colgroup>
    <tr style="height:640px"><th>無料の団信</th><td>
      <div class="center">一般団信<br>(借入時年齢:65歳以下)<br>+がん50%保障団信<br>(借入時年齢:50歳以下)<br>+全疾病保障団信<br>(借入時年齢:50歳以下)<br>+月次返済保障団信<br>(借入時年齢:50歳以下)<br>無料</div>
      <span class="note">(死亡・高度障害と診断された場合、または、すべてのけが・病気で入院が180日超の場合、ローン残高が0円、がんと診断された場合、ローン残高が半分)</span>
    </td></tr>
    <tr style="height:860px"><th>オプション(特約)の団信</th><td>
      <b>・がん100%保障団信<br>　(借入時年齢:50歳以下)</b>
      <span class="rate">上乗せ金利0.10%</span>
      <span class="note">(死亡・高度障害状態、がんと診断された場合、または、すべてのけが・病気で入院が180日超の場合、ローン残高が0円)<br>※2022年5月2日以降借り入れの顧客が対象</span>
      <br><b>・11疾病保障団信<br>　(借入時年齢:50歳以下)</b>
      <span class="rate">上乗せ金利0.20%</span>
      <span class="note">(死亡・高度障害、がんと診断された場合、または、10種類の生活習慣病で入院が180日超の場合、ローン残高が0円)<br>※2022年5月2日以降借り入れの顧客が対象</span>
      <br><b>・ワイド団信<br>　(借入時年齢:65歳未満)</b>
      <span class="rate">上乗せ金利0.30%</span>
      <span class="note">(死亡・高度障害と診断された場合、ローン残高が0円)<br>※2022年5月2日以降借り入れの顧客が対象</span>
    </td></tr>
  </table>
  <a class="more" href="https://kirameki-jutaku.jp/articles/-/584213" style="top:1760px">詳細を見る<svg viewBox="0 0 28 32"><path d="M2 2 L26 16 L2 30Z" fill="#fff"/></svg></a>
</section>

</body>
</html>
```